Larkspur Invitation

Please have the invitation say this
You're Invited to Our End-of-Summer Soirée!

As the summer winds down, we’d love for you to join us for a special evening of networking and good company, hosted by Larkspur Realty and Marcus Pellow with Brightvale Mortgage Solutions.

Date: September 19th, 2024
Time: 4:00 PM - 6:00 PM
Location: The Quillmere by Ashford Boston Downtown, Fennick Yard Kitchen and Bar

We’re offering complimentary drinks, light bites, and an exciting raffle with a fantastic prize up for grabs! So come unwind, connect with fellow professionals, and enjoy a relaxing time together.

We can’t wait to see you there and share a toast to new opportunities!

Please RSVP by September 5th by emailing tamsin@larkspurnorth.example

Please include the Quillmere Hotel Logo, Larkspur Logo and Brightvale Mortgage Solutions Logo. This should be a very classy invitation using navy and gold colors. Possibly herringbone pattern and aesthetic

```html
<!DOCTYPE html>
<html lang="en">
<head>
<meta charset="utf-8">
<title>Larkspur Invitation</title>
<link rel="stylesheet" href="https://fonts.googleapis.com/css2?family=Playfair+Display:wght@700;800&family=Lora:wght@400;500;600;700&display=swap">
<style>
  :root {
    --navy: #1b2a5c;
    --navy-deep: #14204a;
    --blue: #2f4fa8;
    --gold: #c9a24a;
    --gold-light: #e6cd8a;
    --cream: #f7efdb;
    --white: #ffffff;
    --ink: #2a3358;
  }
  * { margin: 0; padding: 0; box-sizing: border-box; }
  html, body { width: 849px; height: 1200px; overflow: hidden; background: var(--cream); }
  .invitation { position: relative; width: 849px; height: 1200px; overflow: hidden; background: var(--cream); font-family: "Lora", Georgia, serif; color: var(--ink); }

  .pattern-field { position: absolute; left: 0; top: 0; width: 849px; height: 860px;
    background: linear-gradient(160deg, #22336b 0%, var(--navy) 45%, var(--navy-deep) 100%); }

  .card { position: absolute; left: 150px; top: 48px; width: 550px; height: 800px;
    background: linear-gradient(180deg, #ffffff 0%, #f5f7fc 100%);
    box-shadow: 0 6px 24px rgba(0,0,0,.25); text-align: center; }

  .headline { font-family: "Playfair Display", Georgia, serif; font-weight: 800; text-transform: uppercase; line-height: 1.15; margin-top: 48px; }
  .headline .lead { display: block; color: var(--navy); font-size: 31px; letter-spacing: .5px; }
  .headline .event { display: block; color: var(--gold); font-size: 31px; letter-spacing: .5px; margin-top: 4px; }

  .intro { font-size: 14.5px; line-height: 1.55; color: var(--ink); width: 420px; margin: 34px auto 0; }

  .when { display: flex; justify-content: center; align-items: stretch; margin-top: 30px; }
  .when-item { width: 200px; font-family: "Playfair Display", Georgia, serif; font-weight: 700; }
  .when-item .label { display: block; color: var(--gold); font-size: 30px; }
  .when-item .value { display: block; color: var(--navy); font-size: 28px; line-height: 1.15; }
  .when-divider { width: 2px; background: var(--gold); margin: 0 22px; }

  .location { font-family: "Lora", Georgia, serif; font-weight: 700; font-size: 19px; text-transform: uppercase; color: var(--navy); line-height: 1.35; width: 440px; margin: 42px auto 0; }
  .location .label { color: var(--gold); }

  .details { font-size: 14.5px; line-height: 1.55; width: 420px; margin: 32px auto 0; color: var(--ink); }

  .waves { position: absolute; left: 0; top: 760px; }

  .closing { position: absolute; left: 0; width: 849px; top: 912px; text-align: center; text-transform: uppercase; }
  .closing .toast { color: var(--blue); font-size: 23px; line-height: 1.3; letter-spacing: .5px; font-weight: 500; }
  .closing .rsvp { color: var(--navy); font-size: 23px; font-weight: 700; line-height: 1.3; margin-top: 20px; }

  .partners { position: absolute; left: 0; top: 1070px; width: 849px; height: 110px; }
  .partner { position: absolute; display: flex; align-items: center; gap: 10px; font-family: "Lora", Georgia, serif; font-weight: 700; color: var(--navy); }
  .partner .mark { border-radius: 50%; background: var(--navy); flex: none; }
  .partner-brightvale { left: 40px; top: 8px; font-size: 16px; }
  .partner-brightvale .mark { width: 74px; height: 74px; }
  .partner-larkspur { left: 345px; top: 14px; flex-direction: column; gap: 8px; font-size: 24px; letter-spacing: 2px; text-transform: uppercase; }
  .partner-larkspur .mark { width: 46px; height: 46px; background: var(--gold); }
  .partner-quillmere { left: 610px; top: 32px; font-size: 32px; color: var(--gold); }
</style>
</head>
<body>
<main class="invitation">
  <div class="pattern-field" role="img" aria-label="Navy herringbone pattern background"></div>

  <section class="card">
    <h1 class="headline">
      <span class="lead">You're Invited to Our</span>
      <span class="event">End-of-Summer Soirée!</span>
    </h1>
    <p class="intro">As the summer winds down, we’d love for you to join us for a special evening of networking and good company, hosted by Larkspur Realty and Marcus Pellow with Brightvale Mortgage Solutions.</p>

    <div class="when">
      <div class="when-item"><span class="label">Date:</span><span class="value">September<br>19th, 2024</span></div>
      <div class="when-divider"></div>
      <div class="when-item"><span class="label">Time:</span><span class="value">4:00 PM -<br>6:00 PM</span></div>
    </div>

    <p class="location"><span class="label">Location:</span> The Quillmere by Ashford Boston Downtown, Fennick Yard Kitchen and Bar</p>

    <p class="details">We’re offering complimentary drinks, light bites, and an exciting raffle with a fantastic prize up for grabs! So come unwind, connect with fellow professionals, and enjoy a relaxing time together.</p>
  </section>

  <svg class="waves" width="849" height="160" viewBox="0 0 849 160" aria-hidden="true">
    <defs>
      <linearGradient id="goldSweep" x1="0" y1="0" x2="1" y2="0">
        <stop offset="0" stop-color="#b8892f"/>
        <stop offset=".5" stop-color="#f0d995"/>
        <stop offset="1" stop-color="#c9a24a"/>
      </linearGradient>
      <linearGradient id="blueSweep" x1="0" y1="0" x2="1" y2="0">
        <stop offset="0" stop-color="#1b2a5c"/>
        <stop offset=".6" stop-color="#2f4fa8"/>
        <stop offset="1" stop-color="#1b2a5c"/>
      </linearGradient>
    </defs>
    <path d="M0 40 C 220 140, 520 10, 849 60 L 849 160 L 0 160 Z" fill="url(#blueSweep)"/>
    <path d="M0 70 C 240 150, 540 40, 849 95 L 849 160 L 0 160 Z" fill="url(#goldSweep)"/>
    <path d="M0 90 C 250 165, 560 70, 849 120 L 849 160 L 0 160 Z" fill="#f7efdb"/>
  </svg>

  <section class="closing">
    <p class="toast">We can’t wait to see you there and share a<br>toast to new opportunities!</p>
    <p class="rsvp">Please RSVP by September 5th by emailing<br>tamsin@larkspurnorth.example</p>
  </section>

  <footer class="partners">
    <div class="partner partner-brightvale"><span class="mark"></span><span>Brightvale</span></div>
    <div class="partner partner-larkspur"><span class="mark"></span><span>Larkspur</span></div>
    <div class="partner partner-quillmere"><span>quillmere</span></div>
  </footer>
</main>
</body>
</html>
```